Velvet Compass - our client magazine

A quality magazine consisting of a number of bespoke articles in the first half followed by an overview of each company that form part of the group as well as details of the services offered. Vast majority of the copy is attached to provide a good overview of the content required. The magazine will require printing so quality imagery is required.

Industry/Entity Type

Recruitment

Font styles to use
Serif

Colors
0355a3
6b449b
3276b5
876aae
a64599
00a990
5c5c5c
000000
474747

Requirements
Must have
• Bringing the copy to life through flow charts and/or diagrams where possible.

```html
<!DOCTYPE html>
<html lang="en">
<head>
<meta charset="utf-8">
<title>Velvet Compass – Introduction &amp; Contents</title>
<link href="https://fonts.googleapis.com/css2?family=Cormorant+Garamond:ital,wght@0,400;0,500;0,600;1,400&family=EB+Garamond:ital,wght@0,400;0,600;1,400&family=Cormorant+SC:wght@600&display=swap" rel="stylesheet">
<style>
  :root{
    --band:#c6c6c6;
    --paper:#ffffff;
    --ink:#1a1a1a;
    --text:#2b2b2b;
    --muted:#474747;
    --rule:#c9c9c9;
    --accent:#7ed321;
    --photo-dark:#141414;
    --photo-mid:#2a2a2a;
  }
  *{margin:0;padding:0;box-sizing:border-box}
  html,body{width:1200px;height:799px;overflow:hidden;background:var(--paper)}
  .spread{position:relative;width:1200px;height:799px;background:var(--paper);color:var(--text);font-family:"EB Garamond",Georgia,serif}
  .band{position:absolute;left:0;width:100%;background:var(--band)}
  .band--top{top:0;height:12px}
  .band--bottom{bottom:0;height:11px}

  /* left page */
  .side-brand{position:absolute;left:92px;top:296px;transform-origin:0 0;transform:rotate(-90deg);
    font-family:"Cormorant Garamond",serif;font-weight:600;font-size:17px;letter-spacing:3px;color:var(--accent);white-space:nowrap;line-height:1}
  .side-title{position:absolute;left:71px;top:690px;transform-origin:0 0;transform:rotate(-90deg);
    font-family:"Cormorant Garamond",serif;font-weight:500;font-size:38px;color:var(--ink);white-space:nowrap;line-height:1}
  .portrait{position:absolute;left:157px;top:95px;width:361px;height:184px;
    background:radial-gradient(ellipse at 55% 60%,#3c3f4a 0%,var(--photo-mid) 35%,var(--photo-dark) 75%)}
  .portrait__caption{position:absolute;left:11px;bottom:12px;font-size:9px;color:#f2f2f2}
  .letter{position:absolute;left:157px;top:312px;width:361px;font-size:9.2px;line-height:13.6px;text-align:justify}
  .letter p{margin-bottom:13.6px}
  .letter .sign{text-align:left;margin-bottom:0}
  .page-num{position:absolute;top:753px;font-size:11px;color:var(--muted)}

  /* right page */
  .brand{position:absolute;left:682px;width:419px;top:60px;text-align:center;
    font-family:"Cormorant Garamond",serif;font-weight:600;font-size:26px;letter-spacing:1px;color:var(--accent);line-height:1}
  .toc-title{position:absolute;left:682px;width:419px;top:108px;text-align:center;
    font-family:"Cormorant Garamond",serif;font-weight:500;font-size:36px;color:var(--ink);line-height:1.1}
  .toc-title em{font-style:italic}
  .feature{position:absolute;left:682px;top:181px;width:419px;height:170px;
    background:linear-gradient(180deg,#bdbdbd 0%,#a9a9a9 55%,#2a2a2a 72%,#161616 100%)}
  .toc-row{position:absolute;left:682px;width:419px;border-bottom:1px solid var(--rule);height:22px}
  .toc-row__num{position:absolute;left:0;top:4px;font-size:9px;letter-spacing:1px;color:var(--ink)}
  .toc-row__name{position:absolute;left:116px;top:0;font-family:"Cormorant SC",serif;font-weight:600;font-size:12px;letter-spacing:2px;color:var(--ink)}
  .toc-desc{position:absolute;left:798px;width:303px;font-family:"Cormorant Garamond",serif;font-size:11.5px;line-height:18px;letter-spacing:0.8px;color:var(--ink)}
  .toc-desc em{font-style:italic}
</style>
</head>
<body>
<main class="spread">
  <div class="band band--top"></div>

  <section class="page page--intro">
    <div class="side-brand">VELVET COMPASS</div>
    <h1 class="side-title">Introduction</h1>
    <div class="portrait" role="img" aria-label="Portrait of the co-founder in a grey suit against a dark background">
      <span class="portrait__caption">Martin Hale</span>
    </div>
    <div class="letter">
      <p>Hello and welcome to this latest edition of Velvet Compass.</p>
      <p>In this issue, we are considering the importance of “brand” throughout the recruitment process. As Headhunters, our brand and reputation have always been key to our business. It’s important that candidates know and respect us, and that our clients are happy to recommend us to other companies. However, in recent years it has become increasingly important for both clients and candidates to also consider their own brand very carefully.</p>
      <p>With UK unemployment at record low levels, the competition between companies to attract and retain the top talent is getting fiercer all the time. Candidates will often have multiple job options to choose between. The reputation, culture and working environment of each potential employer therefore needs to be carefully researched to ensure the right choice is made. Developing an attractive and effective Employer Brand and Marketing strategy is therefore essential for all companies.</p>
      <p>On the candidate side, brand is equally important when competing for the most attractive roles. This poses some interesting challenges in the modern world. As social media has become an integral part of life today, the separation between our personal and professional lives is being reduced. Candidates need to be aware that their online life is part of their personal brand and can be important for their career.</p>
      <p>We will consider these issues and more over the next few pages. As always, please do not hesitate to contact us with any questions or comments which arise.</p>
      <p class="sign">I hope you enjoy reading ............. and look forward to working with you soon.<br>Sincerely,</p>
      <p class="sign" style="margin-top:13.6px">Martin Hale<br>Co-Founder &amp; CEO<br>The Norwood Group</p>
    </div>
    <span class="page-num" style="left:297px">2</span>
  </section>

  <section class="page page--contents">
    <div class="brand">VELVET COMPASS</div>
    <h2 class="toc-title">Table <em>of</em> Content</h2>
    <div class="feature" role="img" aria-label="Close-up of a typewriter with the words Build Your Brand typed on paper"></div>

    <div class="toc-row" style="top:412px"><span class="toc-row__num">01.</span><span class="toc-row__name">Doluptat Fugiatemo</span></div>
    <div class="toc-row" style="top:531px"><span class="toc-row__num">17.</span><span class="toc-row__name">Quidundent Ipsum Quiaese</span></div>
    <p class="toc-desc" style="top:569px">Itations equamet officim fuga. Et essumqu isimus deligni am dipsandus aut la core que re.<br><em>rum illiquias et everumquis maio</em></p>
    <div class="toc-row" style="top:648px"><span class="toc-row__num">21.</span><span class="toc-row__name">Obitium Cone Verum</span></div>
    <p class="toc-desc" style="top:686px">Ad ulliae. Et quae volo in coreptata doluptatqui dolo eicto delignis venissi ntibus sa pro tem venda cum as de parum ut ut ex eari cum que re.</p>

    <span class="page-num" style="left:897px">3</span>
  </section>

  <div class="band band--bottom"></div>
</main>
</body>
</html>
```